Modern Business Card for Lanternfield 2018

Our company assumes the best about people. We are creating an online community of entrepreneurs and business leaders who struggle with marketing their business online.

This business card should POP! We recently got a new logo and are launching a new website next month, so our business cards should make a statement that feels:
-Fresh
-Smart
-Trustworthy
-Fun

Target Market(s)

small business owners, entrepreneurs

Industry/Entity Type

Digital Marketing

Contact Information for Business Card

Dimensions: 3.5" x 2"

Font styles to use
Sans Serif

Colors
f37122
ffffff

Requirements
Must have
• We need a business card with a modern, bold design. We will use one side of the card as a lead-generation offer, so text on one side will need to fit up to 140 characters. The business card should stick to our core colors (orange, black, and white).
Nice to have
• We think a vertical "portrait" design could be interesting.
Should not have
• Should not look like a traditional business card. The round icon should stand out from a distance.

```html
<!DOCTYPE html>
<html lang="en">
<head>
<meta charset="utf-8">
<title>Lanternfield Business Card</title>
<link rel="stylesheet" href="https://fonts.googleapis.com/css2?family=Lato:wght@400;700;900&family=Permanent+Marker&display=swap">
<style>
  :root {
    --orange: #f37122;
    --orange-deep: #e85f14;
    --ink: #2a2b2d;
    --ink-edge: #111111;
    --paper: #ffffff;
    --stage: #e9e9eb;
    --text-dark: #1c1c1c;
  }
  * { box-sizing: border-box; margin: 0; padding: 0; }
  html, body { width: 1200px; height: 900px; overflow: hidden; }
  body {
    background: var(--stage);
    font-family: "Lato", sans-serif;
    position: relative;
  }
  .card {
    position: absolute;
    top: 135px;
    width: 360px;
    height: 630px;
    border-radius: 28px;
    overflow: hidden;
    box-shadow: 0 10px 30px rgba(0,0,0,0.18);
  }

  /* Front card */
  .card-front { left: 200px; background: var(--paper); }
  .front-brand {
    position: absolute; top: 80px; left: 0; right: 0;
    display: flex; flex-direction: column; align-items: center; gap: 14px;
  }
  .front-brand .dot {
    width: 120px; height: 120px; border-radius: 50%; background: var(--orange);
  }
  .front-brand .brand-name {
    font-weight: 900; font-size: 26px; letter-spacing: 2px;
    color: var(--orange); text-transform: uppercase;
  }
  .front-shapes { position: absolute; inset: 0; }
  .person-name {
    position: absolute; top: 300px; left: 0; right: 0; text-align: center;
    font-family: "Permanent Marker", sans-serif;
    font-size: 36px; line-height: 48px; height: 48px;
    color: var(--text-dark); letter-spacing: 1px; text-transform: uppercase;
    white-space: nowrap;
  }
  .name-rule {
    position: absolute; top: 362px; left: 135px; width: 90px; height: 3px;
    background: var(--orange);
  }
  .person-role {
    position: absolute; top: 458px; left: 0; right: 0; text-align: center;
    color: var(--paper); font-size: 18px; line-height: 24px; letter-spacing: 0.5px;
  }
  .contact-email {
    position: absolute; top: 538px; left: 0; right: 0;
    display: flex; justify-content: center; align-items: center; gap: 8px;
    font-size: 18px; color: var(--text-dark);
  }

  /* Back card */
  .card-back { left: 640px; background: var(--orange); }
  .back-top {
    position: absolute; top: 0; left: 0; right: 0; height: 228px;
    background: linear-gradient(180deg, var(--orange), var(--orange-deep));
    display: flex; flex-direction: column; align-items: center; justify-content: center; gap: 12px;
    color: var(--paper);
  }
  .back-top .dot { width: 54px; height: 54px; border-radius: 50%; background: var(--paper); }
  .back-top .brand-name {
    font-weight: 900; font-size: 38px; letter-spacing: 2px; text-transform: uppercase;
  }
  .back-top .tagline {
    font-size: 13px; letter-spacing: 2px; text-transform: uppercase; font-weight: 700;
  }
  .back-band {
    position: absolute; top: 228px; left: 0; right: 0; height: 170px;
    background: var(--ink);
    border-top: 6px solid var(--ink-edge); border-bottom: 6px solid var(--ink-edge);
    display: flex; flex-direction: column; align-items: center; justify-content: center;
    color: var(--orange); font-weight: 700; font-size: 21px; line-height: 1.3;
    text-transform: uppercase; text-align: center;
  }
  .back-offer {
    position: absolute; top: 398px; left: 0; right: 0; bottom: 0;
    background: linear-gradient(180deg, var(--orange-deep), var(--orange));
    display: flex; flex-direction: column; align-items: center; justify-content: center;
    color: var(--paper); text-align: center; padding: 0 20px; gap: 10px;
  }
  .back-offer p { font-size: 16px; line-height: 1.45; }
  .back-offer .offer-link { font-weight: 900; font-size: 21px; }
</style>
</head>
<body>

  <section class="card card-front">
    <div class="front-brand">
      <div class="dot"></div>
      <div class="brand-name">Lanternfield</div>
    </div>

    <svg class="front-shapes" width="360" height="630" viewBox="0 0 360 630" aria-hidden="true">
      <path d="M0 394 L0 406 L210 406 L232 394" fill="none" stroke="#f37122" stroke-width="4"/>
      <line x1="290" y1="394" x2="360" y2="394" stroke="#f37122" stroke-width="4"/>
      <path d="M28 510 L28 458 L52 442 L308 442 L332 458 L332 510 Z" fill="#f37122"/>
      <line x1="0" y1="510" x2="28" y2="510" stroke="#f37122" stroke-width="4"/>
      <line x1="332" y1="510" x2="360" y2="510" stroke="#f37122" stroke-width="4"/>
      <line x1="40" y1="595" x2="360" y2="595" stroke="#f37122" stroke-width="4"/>
    </svg>

    <div class="person-name">Dana Whitlow</div>
    <div class="name-rule"></div>
    <div class="person-role">STORY MARKETING COACH</div>
    <div class="contact-email">
      <svg width="20" height="14" viewBox="0 0 20 14" aria-hidden="true">
        <rect x="0" y="0" width="20" height="14" rx="1.5" fill="#f37122"/>
        <path d="M1 1 L10 8 L19 1" fill="none" stroke="#ffffff" stroke-width="1.6"/>
      </svg>
      <span>dana@lanternfieldnow.com</span>
    </div>
  </section>

  <section class="card card-back">
    <div class="back-top">
      <div class="dot"></div>
      <div class="brand-name">Lanternfield</div>
      <div class="tagline">Tell stories that inspire action</div>
    </div>
    <div class="back-band">
      <span>Reach mor people.</span>
      <span>Make more money.</span>
      <span>Create more impact</span>
    </div>
    <div class="back-offer">
      <p>Get your free Lanternfield Starter Package<br>and our marketing guide today at</p>
      <p class="offer-link">lanternfieldnow.com/start</p>
    </div>
  </section>

</body>
</html>
```